Professional Home Buyer business card needed

I need a pretty straight forward business card designed. We help people that NEED to sell their homes solve problems. We perform all types of Real Estate transactions including flip, wholesale, investment, rental property and multi family. The card will mainly be used to give to prospective Sellers but will also be given to Real Estate Investors as well. It should professional and very easy to read, most clients are older people.

Target Market(s)

Distressed home sellers as well as Real Estate investors

Industry/Entity Type

Real Estate

Contact Information for Business Card

should be a professional layout

Colors
ec1f27
ffffff
000000

Requirements
Must have
• Large logo on back and smaller one on front. should utilize Red, white, and black.
• I am thinking of using a soft touch coating on the card so keep that in mind.
• Contact info should be very easy to read, think older clients.
Nice to have
• I would like to see a design with rounded corners on the card
Should not have
• pictures of homes or other home graphics.

```html
<!DOCTYPE html>
<html lang="en">
<head>
<meta charset="utf-8">
<title>Keystone Home Buyers – Business Card</title>
<link href="https://fonts.googleapis.com/css2?family=Montserrat:wght@600;800&family=Poppins:wght@400;500&display=swap" rel="stylesheet">
<style>
  :root {
    --brand-red: #ec1f27;
    --white: #ffffff;
    --black: #000000;
    --card: #0d0d0d;
    --stage: #262626;
    --deboss: #3a3a3a;
    --divider: #555555;
  }
  * { box-sizing: border-box; margin: 0; padding: 0; }
  html, body { width: 1200px; height: 1200px; overflow: hidden; }
  body {
    background: var(--stage);
    font-family: "Poppins", sans-serif;
    color: var(--white);
    position: relative;
  }
  .card {
    position: absolute;
    left: 180px;
    width: 840px;
    height: 480px;
    background: var(--card);
    border-radius: 28px;
  }
  .card--back { top: 90px; }
  .card--front { top: 630px; }

  /* back: large wordmark */
  .wordmark {
    font-family: "Montserrat", sans-serif;
    font-weight: 800;
    text-transform: uppercase;
    line-height: 1;
  }
  .card--back .brand {
    position: absolute;
    inset: 0;
    display: flex;
    align-items: center;
    justify-content: center;
    gap: 26px;
  }
  .card--back .brand-square {
    width: 54px; height: 54px;
    background: var(--brand-red);
  }
  .card--back .wordmark {
    color: var(--deboss);
    font-size: 64px;
    letter-spacing: 2px;
  }
  .card--back .wordmark span { display: block; font-size: 34px; letter-spacing: 12px; margin-top: 12px; }

  /* front */
  .card--front .brand {
    position: absolute;
    left: 60px; top: 0; bottom: 0;
    width: 320px;
    display: flex;
    align-items: center;
    gap: 18px;
  }
  .card--front .brand-square {
    width: 30px; height: 30px; flex: none;
    background: var(--brand-red);
  }
  .card--front .wordmark { color: var(--white); font-size: 38px; }
  .card--front .wordmark span { display: block; font-size: 20px; letter-spacing: 7px; margin-top: 8px; }

  .divider {
    position: absolute;
    left: 405px; top: 130px;
    width: 1px; height: 220px;
    background: var(--divider);
  }
  .contact {
    position: absolute;
    left: 445px; top: 120px;
  }
  .contact-name {
    font-family: "Montserrat", sans-serif;
    font-weight: 800;
    font-size: 30px;
    letter-spacing: 1px;
    text-transform: uppercase;
  }
  .contact-title {
    font-family: "Montserrat", sans-serif;
    font-weight: 600;
    font-size: 19px;
    color: var(--brand-red);
    text-transform: uppercase;
    letter-spacing: 1px;
    margin-bottom: 22px;
  }
  .contact-list { list-style: none; }
  .contact-list li {
    display: flex;
    align-items: center;
    gap: 14px;
    font-size: 19px;
    line-height: 1.2;
    margin-bottom: 12px;
  }
  .contact-list svg { width: 20px; height: 20px; flex: none; fill: var(--brand-red); }
</style>
</head>
<body>

<section class="card card--back" aria-label="Card back">
  <div class="brand">
    <div class="brand-square"></div>
    <div class="wordmark">Keystone<span>Home Buyers</span></div>
  </div>
</section>

<section class="card card--front" aria-label="Card front">
  <div class="brand">
    <div class="brand-square"></div>
    <div class="wordmark">Keystone<span>Home Buyers</span></div>
  </div>

  <div class="divider"></div>

  <div class="contact">
    <h1 class="contact-name">Daniel Harlow</h1>
    <p class="contact-title">President</p>
    <ul class="contact-list">
      <li>
        <svg viewBox="0 0 24 24" aria-hidden="true"><path d="M6.6 10.8a15.1 15.1 0 0 0 6.6 6.6l2.2-2.2c.3-.3.7-.4 1-.2 1.1.4 2.3.6 3.6.6.6 0 1 .4 1 1V20c0 .6-.4 1-1 1A17 17 0 0 1 3 4c0-.6.4-1 1-1h3.5c.6 0 1 .4 1 1 0 1.3.2 2.5.6 3.6.1.3 0 .7-.2 1z"/></svg>
        555-014-2386
      </li>
      <li>
        <svg viewBox="0 0 24 24" aria-hidden="true"><path d="M2 5h20v14H2zm2 2v.5l8 5 8-5V7zm0 2.8V17h16V9.8l-8 5z"/></svg>
        dan@plainshomesforcash.com
      </li>
      <li>
        <svg viewBox="0 0 24 24" aria-hidden="true"><path d="M12 2a10 10 0 1 0 0 20 10 10 0 0 0 0-20zm6.9 6h-3a15.6 15.6 0 0 0-1.3-3.9A8 8 0 0 1 18.9 8zM12 4c.8 1.2 1.5 2.5 1.9 4h-3.8c.4-1.5 1.1-2.8 1.9-4zM4.3 14a8 8 0 0 1 0-4h3.4a16.5 16.5 0 0 0 0 4zm.8 2h3c.3 1.4.8 2.7 1.3 3.9A8 8 0 0 1 5.1 16zm3-8h-3a8 8 0 0 1 4.3-3.9C8.9 5.3 8.4 6.6 8.1 8zM12 20c-.8-1.2-1.5-2.5-1.9-4h3.8c-.4 1.5-1.1 2.8-1.9 4zm2.3-6H9.7a14.7 14.7 0 0 1 0-4h4.6a14.7 14.7 0 0 1 0 4zm.3 5.9c.5-1.2 1-2.5 1.3-3.9h3a8 8 0 0 1-4.3 3.9zm1.7-5.9a16.5 16.5 0 0 0 0-4h3.4a8 8 0 0 1 0 4z"/></svg>
        www.plainshomesforcash.com
      </li>
      <li>
        <svg viewBox="0 0 24 24" aria-hidden="true"><path d="M12 2a7 7 0 0 0-7 7c0 5.2 7 13 7 13s7-7.8 7-13a7 7 0 0 0-7-7zm0 9.5a2.5 2.5 0 1 1 0-5 2.5 2.5 0 0 1 0 5z"/></svg>
        P.O. Box 18, Millbrook, KS 67000
      </li>
    </ul>
  </div>
</section>

</body>
</html>
```